Bright Oak Family Dentistry
Logo For Dental Office - Medical
Logo For Dental Office
Professional
Mira Tolvanen
DMD
2687 Pemberly Lane Suite 214 Virginia Beach, VA 23461
brightoak482@mailnest.com
brightoakfamilydentistry.com
I would like shades of blue in my logo
Appointment card on the back
kivo-darrel kivo-darrel
Can you give me an existing copy of your logo.
lumengrit lumengrit
Hello sir, Can you please provide your logo? :)

```html
<!DOCTYPE html>
<html lang="en">
<head>
<meta charset="utf-8">
<title>Mira Tolvanen DMD – Bright Oak Family Dentistry</title>
<link rel="stylesheet" href="https://fonts.googleapis.com/css2?family=Crimson+Text:wght@400&display=swap">
<style>
  :root {
    --page: #ffffff;
    --card: #ffffff;
    --card-edge: #4a4a4a;
    --brand: #3b3b8e;
    --ink: #1d1d1d;
  }
  html, body {
    margin: 0;
    padding: 0;
    width: 1200px;
    height: 758px;
    overflow: hidden;
    background: var(--page);
  }
  .canvas {
    position: relative;
    width: 1200px;
    height: 758px;
    font-family: "Crimson Text", "Times New Roman", serif;
  }
  .business-card {
    position: absolute;
    left: 132px;
    top: 115px;
    width: 934px;
    height: 530px;
    box-sizing: border-box;
    border: 2px solid var(--card-edge);
    background: var(--card);
    overflow: hidden;
  }
  .doctor-name {
    position: absolute;
    left: 447px;
    top: 78px;
    margin: 0;
    font-weight: 400;
    font-size: 60px;
    line-height: 1;
    color: var(--brand);
    letter-spacing: 0.5px;
    white-space: nowrap;
  }
  .doctor-name .credential {
    font-size: 38px;
    margin-left: 6px;
  }
  .practice-name {
    position: absolute;
    left: 28px;
    top: 248px;
    margin: 0;
    font-weight: 400;
    font-size: 44px;
    line-height: 46px;
    color: var(--brand);
    white-space: nowrap;
  }
  .address {
    position: absolute;
    left: 22px;
    top: 386px;
    margin: 0;
    font-style: normal;
    font-size: 31px;
    line-height: 36px;
    color: var(--ink);
    white-space: nowrap;
  }
  .contact {
    position: absolute;
    left: 485px;
    top: 414px;
    margin: 0;
    font-size: 27px;
    line-height: 38px;
    color: var(--ink);
    white-space: nowrap;
  }
  .base-band {
    position: absolute;
    left: 0;
    right: 0;
    bottom: 0;
    height: 32px;
    background: var(--brand);
  }
</style>
</head>
<body>
  <main class="canvas">
    <section class="business-card">
      <h1 class="doctor-name">Mira Tolvanen<span class="credential">DMD</span></h1>

      <p class="practice-name">Bright Oak<br>Family Dentistry</p>

      <address class="address">
        2687 Pemberly Lane<br>
        Suite 214, Virginia Beach,<br>
        VA 23461, Ph: 757-555-0148
      </address>

      <p class="contact">
        Email: brightoak482@mailnest.com<br>
        www.brightoakfamilydentistry.com
      </p>

      <div class="base-band"></div>
    </section>
  </main>
</body>
</html>
```